Awesome photographers card for an awesome new business

Double sided business card Black background and silver logo in middle on one side. Details on otherside. please keep it simple

Photographer

Gavin Tolley
0482615073
GavinTolleyPhotography82@lumenpost.com
www.GavinTolleyPhotography.com.au
Instagram _Gavin_tolley

Requirements
Must have
• My logo in Silver
• please use instagram logo instead of "Instagram"

```html
<!DOCTYPE html>
<html lang="en">
<head>
<meta charset="UTF-8">
<title>Gavin Tolley Photography – Business Card</title>
<link rel="stylesheet" href="https://fonts.googleapis.com/css2?family=Montserrat:wght@400;500;600&display=swap">
<style>
  :root {
    --backdrop: #1c1c1e;
    --card: #121213;
    --card-pattern-a: #1d1d1f;
    --card-pattern-b: #0e0e0f;
    --silver: #d9d9d9;
    --white: #f4f4f4;
    --grey: #9a9a9a;
  }
  * { box-sizing: border-box; margin: 0; padding: 0; }
  html, body {
    width: 1200px;
    height: 1200px;
    overflow: hidden;
    background: var(--backdrop);
    font-family: "Montserrat", sans-serif;
  }
  .sheet {
    position: relative;
    width: 1200px;
    height: 1200px;
  }
  .card {
    position: absolute;
    left: 160px;
    width: 880px;
    height: 500px;
    background: var(--card);
    box-shadow: 0 18px 40px rgba(0,0,0,0.55);
    overflow: hidden;
  }
  .card--front { top: 70px; }
  .card--back  { top: 630px; }
  .card-pattern {
    position: absolute;
    inset: 0;
    background:
      radial-gradient(circle at 20% 30%, var(--card-pattern-a) 0%, transparent 45%),
      radial-gradient(circle at 80% 70%, var(--card-pattern-a) 0%, transparent 45%),
      radial-gradient(circle at 50% 50%, #161617 0%, var(--card-pattern-b) 80%);
  }

  /* Front: wordmark */
  .wordmark {
    position: absolute;
    left: 50%;
    top: 50%;
    width: 300px;
    height: 300px;
    transform: translate(-50%, -50%);
    border: 6px solid var(--silver);
    border-radius: 50%;
    display: flex;
    flex-direction: column;
    align-items: center;
    justify-content: center;
    gap: 14px;
    color: var(--silver);
    font-weight: 500;
    text-align: center;
  }
  .wordmark__name {
    font-size: 30px;
    letter-spacing: 5px;
    line-height: 1.25;
  }
  .wordmark__tag {
    font-size: 15px;
    letter-spacing: 6px;
  }

  /* Back: details */
  .details {
    position: absolute;
    inset: 0;
    display: flex;
    flex-direction: column;
    align-items: center;
    justify-content: center;
    text-align: center;
  }
  .details__name {
    color: var(--white);
    font-weight: 600;
    font-size: 36px;
    letter-spacing: 4px;
  }
  .details__role {
    color: var(--grey);
    font-weight: 400;
    font-size: 25px;
    letter-spacing: 4px;
    margin-top: 2px;
  }
  .divider {
    width: 26px;
    height: 2px;
    background: var(--white);
    margin: 22px 0;
  }
  .contact {
    list-style: none;
    color: var(--white);
    font-size: 21px;
    letter-spacing: 1.5px;
    line-height: 1.55;
  }
  .social {
    display: flex;
    align-items: center;
    gap: 12px;
    color: var(--white);
    font-size: 21px;
    letter-spacing: 0.5px;
  }
  .social__mark {
    width: 20px;
    height: 20px;
    background: var(--grey);
    border-radius: 3px;
  }
</style>
</head>
<body>
<main class="sheet">
  <section class="card card--front">
    <div class="card-pattern" role="img" aria-label="Faint dark-grey floral damask pattern across the card"></div>
    <div class="wordmark">
      <span class="wordmark__name">GAVIN<br>TOLLEY</span>
      <span class="wordmark__tag">PHOTOGRAPHY</span>
    </div>
  </section>

  <section class="card card--back">
    <div class="card-pattern" role="img" aria-label="Faint dark-grey floral damask pattern across the card"></div>
    <div class="details">
      <h1 class="details__name">GAVIN TOLLEY</h1>
      <p class="details__role">PHOTOGRAPHER</p>
      <div class="divider"></div>
      <ul class="contact">
        <li>0482615073</li>
        <li>GavinTolleyPhotography82@lumenpost.com</li>
        <li>www.GavinTolleyPhotography.com.au</li>
      </ul>
      <div class="divider"></div>
      <p class="social"><span class="social__mark"></span>Gavin_tolley</p>
    </div>
  </section>
</main>
</body>
</html>
```